Professional and creative business card design for recruiting service providers

Our company supports German medium-sized companies in filling vacancies promptly. For this we use social media marketing and bring our customers into the visibility.

We want a professional but also creative design for our business cards.

Please look at halvenrick-consult.de to get an impression of our CI.

Target Market(s)

Small and medium-sized companies in Germany from the industry

Industry/Entity Type

Industrie, Handwerk

Contact Information for Business Card

Name, Position, Telefonnummer, Email, Website

Colors
EE7325
F08F49
F5BC92
FAE3D3
FDF4ED

Requirements
Must have
• A picture of the employee and in the style of www.halvenrick-consult.de

```html
<!DOCTYPE html>
<html lang="de">
<head>
<meta charset="utf-8">
<title>Halvenrick Consult – Visitenkarte</title>
<link rel="stylesheet" href="https://fonts.googleapis.com/css2?family=Arimo:wght@400;700&family=Montserrat:wght@700;800&display=swap">
<style>
  :root {
    --orange: #EE7325;
    --orange-deep: #E55B24;
    --orange-light: #F08F49;
    --peach: #F5BC92;
    --cream: #FDF4ED;
    --ink: #2E2E30;
    --charcoal: #3A3B3F;
    --paper: #FFFFFF;
    --backdrop: #E9E9E9;
  }
  * { box-sizing: border-box; margin: 0; padding: 0; }
  html, body { width: 1200px; height: 802px; overflow: hidden; }
  body {
    background: var(--backdrop);
    display: flex; align-items: center; justify-content: center; gap: 40px;
    font-family: "Arimo", Arial, sans-serif;
  }
  .card {
    position: relative; width: 520px; height: 336px; overflow: hidden;
    box-shadow: 0 6px 18px rgba(0,0,0,.18);
  }
  .card-front { background: var(--paper); }
  .card-back {
    background: linear-gradient(135deg, var(--orange-light) 0%, var(--orange-deep) 70%);
    display: flex; align-items: center; justify-content: center;
  }
  .employee-photo {
    position: absolute; left: 300px; top: 22px; width: 205px; height: 200px;
    background: linear-gradient(180deg, #d9c7b8 0%, #2a2b30 70%);
  }
  .front-shapes { position: absolute; inset: 0; }
  .website {
    position: absolute; left: 334px; top: 282px;
    transform: rotate(-31.25deg); transform-origin: left top;
    color: var(--paper); font-size: 13px; line-height: 1; white-space: nowrap;
  }
  .brand { display: flex; align-items: center; gap: 12px; }
  .brand-mark { width: 34px; height: 34px; background: var(--orange); flex: none; }
  .brand-name {
    font-family: "Montserrat", Arial, sans-serif; font-weight: 800;
    font-size: 19px; line-height: 1.05; letter-spacing: .5px; color: var(--ink);
    text-transform: uppercase;
  }
  .front-content { position: absolute; left: 28px; top: 34px; }
  .person { margin-top: 30px; }
  .person-name { color: var(--orange-deep); font-size: 18px; text-transform: uppercase; letter-spacing: .3px; }
  .person-role { color: var(--ink); font-size: 14px; margin-top: 2px; }
  .address { margin-top: 16px; color: var(--ink); font-size: 13px; line-height: 1.35; }
  .contact { margin-top: 12px; list-style: none; color: var(--ink); font-size: 13px; line-height: 1.5; }
  .contact li { display: flex; align-items: center; gap: 8px; }
  .contact svg { width: 12px; height: 12px; flex: none; }
  .brand-back .brand-mark { background: var(--paper); width: 40px; height: 40px; }
  .brand-back .brand-name { color: var(--paper); font-size: 22px; }
</style>
</head>
<body>
  <article class="card card-front">
    <div class="employee-photo" role="img" aria-label="Portrait photo of the employee"></div>
    <svg class="front-shapes" viewBox="0 0 520 336" aria-hidden="true">
      <polygon points="190,336 520,136 520,160 230,336" fill="var(--charcoal)"/>
      <polygon points="230,336 520,160 520,336" fill="var(--orange-deep)"/>
    </svg>
    <span class="website">www.halvenrick-consult.de</span>
    <div class="front-content">
      <div class="brand">
        <span class="brand-mark"></span>
        <span class="brand-name">Halvenrick<br>Consult</span>
      </div>
      <div class="person">
        <p class="person-name">Lukas Brenner</p>
        <p class="person-role">Manager</p>
      </div>
      <p class="address">Lindenhofer Straße 42b<br>70469 Stuttgart</p>
      <ul class="contact">
        <li>
          <svg viewBox="0 0 24 24"><path d="M6.6 10.8a15 15 0 0 0 6.6 6.6l2.2-2.2a1 1 0 0 1 1-.25 11.4 11.4 0 0 0 3.6.57 1 1 0 0 1 1 1V20a1 1 0 0 1-1 1A17 17 0 0 1 3 4a1 1 0 0 1 1-1h3.5a1 1 0 0 1 1 1c0 1.25.2 2.45.57 3.57a1 1 0 0 1-.25 1z" fill="var(--orange-deep)"/></svg>
          0171 555 2093
        </li>
        <li>
          <svg viewBox="0 0 24 24"><rect x="2" y="5" width="20" height="14" fill="none" stroke="var(--orange-deep)" stroke-width="2.4"/><path d="M2 6l10 7 10-7" fill="none" stroke="var(--orange-deep)" stroke-width="2.4"/></svg>
          info@halvenrick-consult.de
        </li>
      </ul>
    </div>
  </article>

  <article class="card card-back">
    <div class="brand brand-back">
      <span class="brand-mark"></span>
      <span class="brand-name">Halvenrick<br>Consult</span>
    </div>
  </article>
</body>
</html>
```